Magazine Ad for the Waste Industry

We need a full page ad design that will help us introduce our new engine cooling system into the Waste market. This system helps regulate engine temperatures for large trash trucks with its advanced technology and durable. We would like this ad to make an impact and stand out from the more cluttered looking ads that are seen in trade magazines.
The project must be submitted in either InDesign or Photoshop files.

Target Market(s)

Waste Industry, Trash truck manufacturers

Industry/Entity Type

Waste Management

Font styles to use
Sans Serif

Colors
0255a3

Requirements
Must have
• The text and images attached with a more modern industrial/masculine feel.
• Our Company colors are...
• Blue (RGB 25, 76, 159)
• Gray (RGB 129, 130, 133)
• White and black as accents as needed
• SIZING
• Spread Bleed: 9.5" x 11.375"
Nice to have
• I attached two files for a font that we have used in the past. Another font we use commonly is Ariel.

```html
<!DOCTYPE html>
<html lang="en">
<head>
<meta charset="utf-8">
<title>Kestrel Advanced Electric Engine Cooling – Full Page Ad</title>
<link href="https://fonts.googleapis.com/css2?family=Michroma&family=Roboto+Condensed:ital,wght@0,400;0,700;1,400&display=swap" rel="stylesheet">
<style>
  :root{
    --brand-blue:#194c9f;
    --brand-gray:#818285;
    --navy-deep:#0b1220;
    --navy-mid:#1c2740;
    --glow:#4a5a78;
    --white:#ffffff;
    --silver:#c9ccd2;
    --hybrid-yellow:#d9c21c;
    --stage-bg:#e9e7e3;
  }
  *{margin:0;padding:0;box-sizing:border-box}
  html,body{width:1200px;height:960px;overflow:hidden;background:var(--stage-bg)}
  .ad-page{
    position:absolute;left:224px;top:20px;width:752px;height:920px;
    background:
      radial-gradient(ellipse 60% 45% at 50% 64%, var(--glow) 0%, rgba(74,90,120,0) 70%),
      linear-gradient(180deg,var(--navy-mid) 0%,var(--navy-deep) 100%);
    color:var(--white);text-align:center;overflow:hidden;
    font-family:"Roboto Condensed",Arial,sans-serif;
  }
  .brand{position:absolute;top:62px;left:0;right:0}
  .brand-name{
    display:inline-flex;align-items:center;gap:12px;
    font-family:"Michroma",sans-serif;font-size:36px;line-height:1;color:var(--white);
  }
  .brand-name .mark{width:22px;height:22px;background:var(--brand-blue)}
  .brand-tagline{
    margin-top:10px;font-size:12px;letter-spacing:1px;text-transform:uppercase;color:var(--silver);
  }
  .headline{position:absolute;top:158px;left:0;right:0;font-family:"Michroma",sans-serif;font-weight:400;line-height:1}
  .headline-advanced{
    display:block;font-size:80px;letter-spacing:-2px;
    background:linear-gradient(180deg,#ffffff 0%,#8d929c 55%,#dfe2e6 100%);
    -webkit-background-clip:text;background-clip:text;color:transparent;
  }
  .headline-electric{display:block;font-size:54px;color:var(--white);margin-top:6px;letter-spacing:1px}
  .headline-sub{display:block;font-size:21px;color:var(--brand-gray);letter-spacing:12px;margin-top:14px}
  .benefits{
    position:absolute;top:382px;left:60px;right:60px;
    font-size:20px;line-height:1.4;font-style:italic;color:var(--silver);
  }
  .product-visual{
    position:absolute;top:492px;left:196px;width:360px;height:320px;
    background:linear-gradient(160deg,#3a3f48 0%,#16181c 70%);border-radius:4px;
    box-shadow:0 20px 40px rgba(0,0,0,.5);
  }
  .footer{
    position:absolute;bottom:40px;left:60px;right:60px;
    display:flex;justify-content:space-between;align-items:center;
  }
  .web-address{font-size:20px;letter-spacing:1px;color:var(--white)}
  .product-badge{display:flex;align-items:center;gap:10px}
  .product-badge .dot{width:40px;height:40px;border-radius:50%;background:#2c3038}
  .product-badge .label{font-size:22px;font-weight:700;color:var(--hybrid-yellow);letter-spacing:1px}
</style>
</head>
<body>
  <main class="ad-page">
    <header class="brand">
      <div class="brand-name"><span class="mark"></span>KESTREL</div>
      <p class="brand-tagline">Built to Endure</p>
    </header>

    <h1 class="headline">
      <span class="headline-advanced">Advanced</span>
      <span class="headline-electric">electric</span>
      <span class="headline-sub">ENGINE COOLING</span>
    </h1>

    <p class="benefits">• Fully reversible fans • Eliminate preventative<br>maintenance • Average 8% fuel economy • Increase<br>Horsepower • Quieter Residential Operation</p>

    <div class="product-visual" role="img" aria-label="Product photo: black electric engine cooling unit with four fans, lit against the dark background"></div>

    <footer class="footer">
      <span class="web-address">www.kestrel-corp.com/refuse</span>
      <div class="product-badge"><span class="dot"></span><span class="label">DUO-CORE</span></div>
    </footer>
  </main>
</body>
</html>
```